Fatigued and Overloaded by COVID Messages? We need original illustrations to show that.

Everywhere you look there are messages about COVID. That is leading many people to feel fatigued and overloaded by the messages.

We surveyed U.S. adults March 20th - 24th, 2020 and measured message fatigue, information overload, perceived repetition, and perceived exaggeration. Here is how participants responded:

When it comes to coronavirus . . .
55% feel exhausted by all the messages.
54% feel overloaded by the amount of information.
51% feel that the messages are repetitive.
47% feel like messages exaggerate how bad it is.

In other words, almost half of U.S. adults show signs of message fatigue, information overload, perceived message repetition, and perceived message exaggeration.

We will continue to survey 400 adults every week for the next 16 weeks. Each time we will measure message fatigue, information overload, perceived repetition, and perceived exaggeration. We expect that it will increase over time.

What are we looking for? We need innovative and original illustrations that attempt to communicate these findings. The illustrations would visualize message fatigue, information overload, perceived message repetition, and perceived message exaggeration.

What sort of visual are we looking for? Our preference is for an original illustration (or set of illustrations). Our preference is for creative and powerful illustrations, but we are also open to the creative and well-executed infographics.

We need these images fast . We will award monetary prizes to the 3 best designs. If we like more than that, then we might purchase more (e.g., in past contests, we have purchased as many as 30 designs).

What we will need:
(1) The illustrations must be original and we will need the photoshop and/or illustrator files for all artwork. (By original, we mean that the illustrations are 100% created by you. Our organization requires that we utilize only original illustrated work. We have had issues with free imagery being pirated and reposted as free. We sidestep that issue by just having everything created.)

(2) The illustration should say, somewhere: "Based on a survey of 400 U.S. adults conducted March 20 - 24th, 2020."

(3) We will have almost 4 months worth of data by the time this is done. In other words, the illustrations might be able to help us present that weekly data.

(4) We have conducted other Artvendo projects. It might be helpful to examine designs we liked in the past. For example, here is another COVID project we just finished:

https://jobs.artvendo-example.com/job/5162048

Target Market(s)

U.S. adults

Requirements
Must have
• Original illustrations. Mobile friendly design. People will view this on their smartphones.
Nice to have
• A design that we can use to communicate the data across time.

```html
<!DOCTYPE html>
<html lang="en">
<head>
<meta charset="utf-8">
<title>Fatigued and Overloaded by COVID Messages?</title>
<link rel="stylesheet" href="https://fonts.googleapis.com/css2?family=Itim&family=Encode+Sans+Semi+Condensed:wght@500;600&display=block">
<style>
  :root {
    --sky-top: #4634a2;
    --sky-bottom: #6b3dbd;
    --tower: #45269c;
    --tower-roof: #2f1b8c;
    --tower-dark: #2a1a80;
    --city: #5532a8;
    --city-window: #6a44b8;
    --red: #ee3f52;
    --magenta: #c8145e;
    --yellow: #f9cd5c;
    --orange: #ffb300;
    --deep-orange: #fb8c00;
    --awning: #a3a9dc;
    --road: #8361c6;
    --ground: #6334b8;
    --white: #ffffff;
  }
  * { margin: 0; padding: 0; box-sizing: border-box; }
  html, body { width: 1200px; height: 2466px; overflow: hidden; }
  body {
    position: relative;
    background: linear-gradient(180deg, var(--sky-top) 0%, var(--sky-bottom) 100%);
    font-family: "Encode Sans Semi Condensed", "Arial Narrow", Arial, sans-serif;
    color: var(--white);
  }
  .scene { position: absolute; inset: 0; }
  .display { font-family: "Itim", "Comic Sans MS", "Trebuchet MS", sans-serif; font-weight: 400; }
  .headline {
    position: absolute; left: 0; right: 0; top: 38px;
    text-align: center;
    font-size: 88px; line-height: 108px;
  }
  .headline .underlined {
    text-decoration: underline; text-decoration-thickness: 6px; text-underline-offset: 16px;
  }
  .stat-hero {
    position: absolute; left: 763px; top: 1047px; width: 336px; height: 336px;
    display: flex; align-items: center; justify-content: center;
    font-size: 150px; line-height: 1;
  }
  .legend { position: absolute; left: 738px; }
  .legend-item { display: flex; align-items: flex-start; gap: 14px; font-weight: 600; text-transform: uppercase; }
  .legend-swatch { width: 31px; height: 55px; flex: none; }
  .legend-swatch-red { background: var(--red); }
  .legend-swatch-yellow { background: var(--yellow); }
  .legend-exhausted { top: 1399px; font-size: 31px; line-height: 30px; }
  .legend-good { top: 1475px; font-size: 25px; line-height: 30px; }
  .stat {
    position: absolute; left: 730px; width: 366px; text-align: center;
    text-transform: uppercase; font-weight: 600; font-size: 25px; line-height: 24px;
  }
  .stat-badge {
    display: block; margin: 0 auto 10px; width: 106px; height: 106px;
    font-size: 46px; line-height: 106px; text-transform: none;
  }
  .footer {
    position: absolute; left: 0; right: 0; top: 2334px; text-align: center;
    font-size: 56px; line-height: 62px;
  }
</style>
</head>
<body>
<svg class="scene" width="1200" height="2466" viewBox="0 0 1200 2466">
  <defs>
    <linearGradient id="calm-fill" x1="0" y1="0" x2="0" y2="1">
      <stop offset="0" stop-color="var(--orange)"/>
      <stop offset="1" stop-color="var(--deep-orange)"/>
    </linearGradient>
    <linearGradient id="stress-fill" x1="0" y1="0" x2="0" y2="1">
      <stop offset="0" stop-color="var(--red)"/>
      <stop offset="1" stop-color="var(--magenta)"/>
    </linearGradient>
  </defs>

  <!-- background city blocks -->
  <rect x="1015" y="1480" width="185" height="795" fill="var(--city)"/>
  <polygon points="43,1638 144,1700 144,2275 43,2275" fill="var(--city)"/>
  <g fill="var(--city-window)">
    <rect x="1066" y="1580" width="24" height="70"/><rect x="1118" y="1670" width="24" height="70"/>
    <rect x="1066" y="1835" width="24" height="70"/><rect x="1118" y="1835" width="24" height="70"/>
    <rect x="1066" y="2000" width="24" height="70"/><rect x="1118" y="2160" width="24" height="70"/>
    <rect x="65" y="1745" width="24" height="55"/><rect x="65" y="1850" width="24" height="55"/>
    <rect x="65" y="1955" width="24" height="55"/><rect x="110" y="1810" width="24" height="55"/>
    <rect x="110" y="1990" width="24" height="55"/>
  </g>

  <!-- hero illustration areas -->
  <circle cx="853" cy="536" r="290" fill="url(#calm-fill)" role="img" aria-label="Illustration: a calm woman in an orange sweater reading her tablet, a white cat on her shoulder"/>
  <path role="img" aria-label="Illustration: a stressed man with glasses clutching his head at his laptop, surrounded by flying papers and message bubbles"
        d="M160,278 C250,240 320,350 420,352 C520,354 600,250 660,262 C715,275 680,360 620,420 C560,480 545,560 600,620 C650,675 730,690 748,790 C765,880 700,900 640,880 C560,858 520,905 450,915 C350,930 250,945 170,910 C90,875 70,790 52,690 C35,600 70,560 110,480 C140,420 110,305 160,278 Z"
        fill="url(#stress-fill)" stroke="var(--white)" stroke-width="12" stroke-linejoin="round"/>

  <!-- dashed arrow -->
  <path d="M700,881 C770,920 820,980 833,1054" fill="none" stroke="var(--white)" stroke-width="7" stroke-dasharray="22 16" stroke-linecap="round"/>
  <path d="M770,1000 L833,1060 L873,970" fill="none" stroke="var(--white)" stroke-width="7" stroke-linecap="round" stroke-linejoin="round"/>

  <!-- hero stat ring -->
  <circle cx="931" cy="1215" r="168" fill="var(--red)"/>
  <path d="M931,1041 A174,174 0 1,1 877,1381" fill="none" stroke="var(--white)" stroke-width="9" stroke-linecap="round"/>

  <!-- small stat rings -->
  <g fill="var(--red)">
    <circle cx="910" cy="1619" r="50"/><circle cx="910" cy="1815" r="50"/><circle cx="910" cy="2012" r="50"/>
  </g>
  <g fill="none" stroke="var(--white)" stroke-width="5" stroke-linecap="round">
    <path d="M910,1565 A54,54 0 1,1 905,1673"/>
    <path d="M910,1761 A54,54 0 1,1 885,1863"/>
    <path d="M910,1958 A54,54 0 1,1 924,2064"/>
  </g>

  <!-- tower -->
  <rect x="223" y="1004" width="387" height="79" fill="var(--tower-roof)"/>
  <rect x="144" y="1081" width="542" height="1194" fill="var(--tower)"/>
  <g class="tower-windows">
    <g transform="translate(0,1219)">
      <rect x="198" width="31" height="55" fill="var(--yellow)"/><rect x="243" width="31" height="55" fill="var(--red)"/><rect x="287" width="31" height="55" fill="var(--yellow)"/><rect x="332" width="31" height="55" fill="var(--yellow)"/><rect x="377" width="31" height="55" fill="var(--red)"/><rect x="422" width="31" height="55" fill="var(--yellow)"/><rect x="466" width="31" height="55" fill="var(--yellow)"/><rect x="511" width="31" height="55" fill="var(--red)"/><rect x="556" width="31" height="55" fill="var(--red)"/><rect x="600" width="31" height="55" fill="var(--red)"/></g>
    <g transform="translate(0,1313)">
      <rect x="198" width="31" height="55" fill="var(--red)"/><rect x="243" width="31" height="55" fill="var(--red)"/><rect x="287" width="31" height="55" fill="var(--yellow)"/><rect x="332" width="31" height="55" fill="var(--red)"/><rect x="377" width="31" height="55" fill="var(--yellow)"/><rect x="422" width="31" height="55" fill="var(--red)"/><rect x="466" width="31" height="55" fill="var(--yellow)"/><rect x="511" width="31" height="55" fill="var(--yellow)"/><rect x="556" width="31" height="55" fill="var(--red)"/><rect x="600" width="31" height="55" fill="var(--red)"/></g>
    <g transform="translate(0,1408)">
      <rect x="198" width="31" height="55" fill="var(--yellow)"/><rect x="243" width="31" height="55" fill="var(--yellow)"/><rect x="287" width="31" height="55" fill="var(--yellow)"/><rect x="332" width="31" height="55" fill="var(--red)"/><rect x="377" width="31" height="55" fill="var(--red)"/><rect x="422" width="31" height="55" fill="var(--red)"/><rect x="466" width="31" height="55" fill="var(--yellow)"/><rect x="511" width="31" height="55" fill="var(--yellow)"/><rect x="556" width="31" height="55" fill="var(--red)"/><rect x="600" width="31" height="55" fill="var(--yellow)"/></g>
    <g transform="translate(0,1502)">
      <rect x="198" width="31" height="55" fill="var(--red)"/><rect x="243" width="31" height="55" fill="var(--yellow)"/><rect x="287" width="31" height="55" fill="var(--yellow)"/><rect x="332" width="31" height="55" fill="var(--red)"/><rect x="377" width="31" height="55" fill="var(--red)"/><rect x="422" width="31" height="55" fill="var(--yellow)"/><rect x="466" width="31" height="55" fill="var(--yellow)"/><rect x="511" width="31" height="55" fill="var(--red)"/><rect x="556" width="31" height="55" fill="var(--yellow)"/><rect x="600" width="31" height="55" fill="var(--red)"/></g>
    <g transform="translate(0,1597)">
      <rect x="198" width="31" height="55" fill="var(--red)"/><rect x="243" width="31" height="55" fill="var(--red)"/><rect x="287" width="31" height="55" fill="var(--yellow)"/><rect x="332" width="31" height="55" fill="var(--red)"/><rect x="377" width="31" height="55" fill="var(--yellow)"/><rect x="422" width="31" height="55" fill="var(--red)"/><rect x="466" width="31" height="55" fill="var(--red)"/><rect x="511" width="31" height="55" fill="var(--red)"/><rect x="556" width="31" height="55" fill="var(--red)"/><rect x="600" width="31" height="55" fill="var(--red)"/></g>
    <g transform="translate(0,1691)">
      <rect x="198" width="31" height="55" fill="var(--red)"/><rect x="243" width="31" height="55" fill="var(--yellow)"/><rect x="287" width="31" height="55" fill="var(--yellow)"/><rect x="332" width="31" height="55" fill="var(--red)"/><rect x="377" width="31" height="55" fill="var(--red)"/><rect x="422" width="31" height="55" fill="var(--yellow)"/><rect x="466" width="31" height="55" fill="var(--red)"/><rect x="511" width="31" height="55" fill="var(--red)"/><rect x="556" width="31" height="55" fill="var(--yellow)"/><rect x="600" width="31" height="55" fill="var(--red)"/></g>
    <g transform="translate(0,1786)">
      <rect x="198" width="31" height="55" fill="var(--yellow)"/><rect x="243" width="31" height="55" fill="var(--red)"/><rect x="287" width="31" height="55" fill="var(--red)"/><rect x="332" width="31" height="55" fill="var(--yellow)"/><rect x="377" width="31" height="55" fill="var(--yellow)"/><rect x="422" width="31" height="55" fill="var(--yellow)"/><rect x="466" width="31" height="55" fill="var(--red)"/><rect x="511" width="31" height="55" fill="var(--red)"/><rect x="556" width="31" height="55" fill="var(--yellow)"/><rect x="600" width="31" height="55" fill="var(--yellow)"/></g>
    <g transform="translate(0,1880)">
      <rect x="198" width="31" height="55" fill="var(--yellow)"/><rect x="243" width="31" height="55" fill="var(--red)"/><rect x="287" width="31" height="55" fill="var(--yellow)"/><rect x="332" width="31" height="55" fill="var(--red)"/><rect x="377" width="31" height="55" fill="var(--red)"/><rect x="422" width="31" height="55" fill="var(--yellow)"/><rect x="466" width="31" height="55" fill="var(--red)"/><rect x="511" width="31" height="55" fill="var(--yellow)"/><rect x="556" width="31" height="55" fill="var(--yellow)"/><rect x="600" width="31" height="55" fill="var(--red)"/></g>
    <g transform="translate(0,1975)">
      <rect x="198" width="31" height="55" fill="var(--yellow)"/><rect x="243" width="31" height="55" fill="var(--red)"/><rect x="287" width="31" height="55" fill="var(--yellow)"/><rect x="332" width="31" height="55" fill="var(--red)"/><rect x="377" width="31" height="55" fill="var(--red)"/><rect x="422" width="31" height="55" fill="var(--yellow)"/><rect x="466" width="31" height="55" fill="var(--red)"/><rect x="511" width="31" height="55" fill="var(--red)"/><rect x="556" width="31" height="55" fill="var(--yellow)"/><rect x="600" width="31" height="55" fill="var(--red)"/></g>
    <g transform="translate(0,2069)">
      <rect x="198" width="31" height="55" fill="var(--red)"/><rect x="243" width="31" height="55" fill="var(--red)"/><rect x="287" width="31" height="55" fill="var(--yellow)"/><rect x="332" width="31" height="55" fill="var(--yellow)"/><rect x="377" width="31" height="55" fill="var(--red)"/><rect x="422" width="31" height="55" fill="var(--yellow)"/><rect x="466" width="31" height="55" fill="var(--red)"/><rect x="511" width="31" height="55" fill="var(--yellow)"/><rect x="556" width="31" height="55" fill="var(--red)"/><rect x="600" width="31" height="55" fill="var(--red)"/></g>
  </g>

  <!-- storefronts -->
  <rect x="151" y="2160" width="208" height="53" rx="6" fill="var(--awning)"/>
  <rect x="468" y="2160" width="207" height="53" rx="6" fill="var(--awning)"/>
  <rect x="171" y="2213" width="161" height="46" fill="var(--tower-dark)"/>
  <rect x="492" y="2213" width="161" height="46" fill="var(--tower-dark)"/>
  <rect x="380" y="2170" width="73" height="105" fill="var(--tower-dark)"/>

  <!-- street -->
  <rect x="0" y="2275" width="1200" height="58" fill="var(--road)"/>
  <line x1="0" y1="2302" x2="1200" y2="2302" stroke="#b9a3e6" stroke-width="3" stroke-dasharray="34 50"/>
  <rect x="0" y="2333" width="1200" height="133" fill="var(--ground)"/>
</svg>

<h1 class="headline display">Fatigued and Overloaded<br>by <span class="underlined">COVID</span> Messages?</h1>

<div class="stat-hero display">55%</div>

<div class="legend legend-exhausted legend-item"><span class="legend-swatch legend-swatch-red"></span><span>Feel exhausted by<br>all the messages</span></div>
<div class="legend legend-good legend-item"><span class="legend-swatch legend-swatch-yellow"></span><span>Feel good</span></div>

<div class="stat" style="top:1566px"><span class="stat-badge display">54%</span>Feel overloaded by the<br>amount of information</div>
<div class="stat" style="top:1762px"><span class="stat-badge display">51%</span>Feel that the messages<br>are repetitive</div>
<div class="stat" style="top:1959px"><span class="stat-badge display">47%</span>Feel like messages<br>exaggerate how bad it is</div>

<p class="footer display">Based on a survey of 400 U.S. adults<br>conducted March 20–24th, 2020.</p>
</body>
</html>
```